Freelance Translator in Need of a Business Card

I am a freelance Japanese to English translator. I work in the video game localization industry and do literary translation in my spare time. I would like to have both the English word 'Translator' and the Japanese '翻訳者' in the job title. The final design should evoke trust, openness, and reliability.

Target Market(s)

Video game localization companies
Japanese comic book artists

Industry/Entity Type

Business

Contact Information for Business Card

Daniel Oskerby, Translator
dan.oskerby@fernlowmail.com
velmotranslates.com
twitter: @velmo_tl

Colors

Designer to choose colors to be used in the design.

```html
<!DOCTYPE html>
<html lang="en">
<head>
<meta charset="utf-8">
<title>Daniel Oskerby — Translator Business Card</title>
<link rel="stylesheet" href="https://fonts.googleapis.com/css2?family=Montserrat:wght@600;700&family=Questrial&family=Noto+Sans+JP:wght@400&display=swap">
<style>
  :root {
    --backdrop: #b8743f;
    --card-black: #030507;
    --card-white: #ffffff;
    --ink: #111111;
    --paper-text: #ffffff;
    --accent-red: #e3202b;
  }
  * { margin: 0; padding: 0; box-sizing: border-box; }
  html, body {
    width: 1200px; height: 1200px; overflow: hidden;
    background: var(--backdrop);
  }
  .canvas { position: relative; width: 1200px; height: 1200px; }
  .card {
    position: absolute; top: 231px; width: 429px; height: 686px;
  }
  .card--front { left: 133px; background: var(--card-black); }
  .card--back { left: 620px; background: var(--card-white); }

  .brand-name {
    position: absolute; left: 44px; top: 97px;
    font-family: "Montserrat", sans-serif; font-weight: 600;
    font-size: 27px; letter-spacing: 0.5px;
    color: var(--paper-text);
  }
  .website {
    position: absolute; left: 42px; top: 541px;
    font-family: "Questrial", sans-serif; font-size: 24.5px;
    color: var(--paper-text); letter-spacing: 0.3px;
  }
  .website .dot { color: var(--accent-red); }

  .identity {
    position: absolute; left: 0; right: 0; top: 117px;
    text-align: center;
  }
  .person-name {
    font-family: "Montserrat", sans-serif; font-weight: 700;
    font-size: 26px; font-variant: small-caps; letter-spacing: 0.6px;
    color: var(--ink); line-height: 32px;
  }
  .job-title {
    font-family: "Questrial", sans-serif; font-size: 27px;
    color: var(--ink); line-height: 34px; letter-spacing: 0.2px;
  }
  .job-title .ja {
    font-family: "Noto Sans JP", sans-serif; color: var(--accent-red);
    margin-right: 4px;
  }

  .contact-row {
    position: absolute; left: 20px; top: 560px;
    display: flex; align-items: center;
    font-family: "Questrial", sans-serif; font-size: 15.5px; color: var(--ink);
  }
  .contact-row svg { display: block; }
  .contact-email { margin-left: 5px; }
  .handle-mark {
    width: 26px; height: 26px; border-radius: 50%;
    background: var(--ink); margin-left: 12px;
  }
  .contact-handle { margin-left: 6px; }
</style>
</head>
<body>
<main class="canvas">
  <section class="card card--front">
    <div class="brand-name">VELMOTRANSLATES</div>
    <div class="website">www<span class="dot">.</span>velmotranslates<span class="dot">.</span>com</div>
  </section>

  <section class="card card--back">
    <div class="identity">
      <div class="person-name">Daniel Oskerby</div>
      <div class="job-title"><span class="ja">翻訳者</span>TRANSLATOR</div>
    </div>
    <div class="contact-row">
      <svg class="icon-mail" width="31" height="21" viewBox="0 0 31 21" aria-hidden="true">
        <rect x="1" y="1" width="29" height="19" rx="2" fill="none" stroke="#111" stroke-width="2"/>
        <path d="M1.5 2 L15.5 12 L29.5 2 M1.5 19 L11 10 M29.5 19 L20 10" fill="none" stroke="#111" stroke-width="2"/>
      </svg>
      <span class="contact-email">dan.oskerby@fernlowmail.com</span>
      <span class="handle-mark" aria-hidden="true"></span>
      <span class="contact-handle">@velmo_tl</span>
    </div>
  </section>
</main>
</body>
</html>
```